依頼概要
クラシックCDのジャケットのデザインをお願いします。

・ジャケット(4ページ)
・バックカード
・キャップ
・CDの盤面
・facebook用カバー写真

各サイズは添付のジャケットサイズを参照お願いします。

ジャケットタイトルは「HOTAMINE」で春の桜をイメージしたデザインをお願いします。

メインとなる曲は「ホタミネ」というオリジナル曲で青春の輝きをイメージした曲です。
桜の美しさと儚さに、青春の輝きと儚さを重ね合わせ、夢を叶えたい若者の姿を表しています。

デザインの参考として下記のサイトのようなスタイリッシュなものを希望します。
http://www.kestrova.co.jp/anniversary/archives/athlete.html

http://www.tasukemo.jp/work/detail/804127

また、添付の「サンプル.jpg」のような「HOTAMINE」の文字と桜の背景を組み合わせたデザインもかっこいいと思うので送付します。

■アーティスト情報

タイトル:「HOTAMINE」
出版者名:Marlowe Guild

■各ページの内容

【1ページ目(ジャケット表面)】
上記のサイトやサンプルを参考にしてスタイリッシュなデザインをお願いします。表面には出演者の写真は使用なしでお願いします。

【2ページ目】
添付の収録曲を記載してデザインお願いします。

【3ページ目】
作曲者2名の写真を添付しますので、こちらのうちいくつかを使用してデザインお願いします。

【4ページ目】
オリジナル曲「遠い灯台」の歌詞(仮)を添付しますので、こちらを使用して自由や翼、空をモチーフとしたデザインをお願いします。

【バックカード】
添付の収録曲を記載してデザインお願いします。

■補足事項

・文字情報や写真入れ替えなど修正が入る場合がありますので、変更しやすいようにPhotoshopでのデータ構成をお願いします。
・収録曲名と歌詞については正式版に後ほど差し替えをお願いします。
・ロゴを現在制作中で、できましたら送付しますので組み込みをお願いします。
・ジャケット表面と同じデザインでfacebookカバー写真(851px × 315px)も作成お願いします。こちらは採用が決定してからで大丈夫です

今後CDをいくつかリリースする予定ですので、素敵なデザインができる方には続けて依頼したいと思っています。
どうぞよろしくお願いいたします。
以下の資料を添付します。

・ジャケットサイズ
・作曲者写真
・収録曲
・遠い灯台歌詞
・サンプル画像
作曲者写真を追加しますのでこちらもご検討お願いします。
桜の画像を用意しましたので、よろしければこちらを使っていただければと思います。

それから、ロゴのデザインができましたので添付いたします。
Marlowe Guildというロゴをジャケット表面、盤面、帯に入れていただきますようお願いします。
ジャケット表面は添付のspringのような少し文字と桜が絡み合うようなデザイン性のある作品を希望いたします。凝った技術が必要と思いますがご提案いただけたら幸いです。

とても洗練されたデザインでした。

たくさんのご提案ありがとうございます。

```html
<!DOCTYPE html>
<html lang="ja">
<head>
<meta charset="utf-8">
<title>HOTAMINE — CD Cap</title>
<link href="https://fonts.googleapis.com/css2?family=Cormorant+Garamond:wght@300;400&family=Noto+Serif+JP:wght@300;400&family=Noto+Sans+JP:wght@400&display=swap" rel="stylesheet">
<style>
  :root {
    --paper: #ffffff;
    --frame: #d9d9d9;
    --grad-left: #e5e7f5;
    --grad-right: #f3dbe3;
    --spine: #f7e4ea;
    --spine-line: #e3c2cc;
    --rose: #e8b7c2;
    --rose-text: #ffffff;
    --mauve: #b98f9b;
    --pink-ink: #d08c9e;
    --caption: #444444;
  }
  html, body {
    margin: 0;
    padding: 0;
    width: 797px;
    height: 1200px;
    overflow: hidden;
    background: var(--paper);
  }
  .sheet {
    position: relative;
    width: 797px;
    height: 1200px;
  }
  .sheet-frame {
    position: absolute;
    left: 53px;
    top: 53px;
    width: 692px;
    height: 1075px;
    border: 1px solid var(--frame);
    box-sizing: border-box;
  }
  .cap {
    position: absolute;
    left: 165px;
    top: 120px;
    height: 865px;
    display: flex;
  }
  .cap-front {
    width: 266px;
    height: 100%;
    background: linear-gradient(90deg, var(--grad-left) 0%, var(--grad-left) 15%, var(--grad-right) 100%);
  }
  .cap-spine {
    position: relative;
    width: 90px;
    height: 100%;
    background: var(--spine);
    border-left: 1px solid var(--spine-line);
    border-right: 1px solid var(--spine-line);
    box-sizing: border-box;
  }
  .cap-back {
    position: relative;
    width: 107px;
    height: 100%;
    background: var(--rose);
  }
  .brand {
    position: absolute;
    top: 32px;
    left: 0;
    right: 0;
    display: flex;
    flex-direction: column;
    align-items: center;
    gap: 5px;
  }
  .brand-dot {
    width: 18px;
    height: 18px;
    border-radius: 50%;
    border: 1.5px solid currentColor;
    box-sizing: border-box;
  }
  .brand-name {
    font-family: "Cormorant Garamond", serif;
    font-weight: 400;
    font-size: 8px;
    letter-spacing: 0.05em;
    white-space: nowrap;
  }
  .cap-spine .brand { color: var(--mauve); }
  .cap-back .brand { color: var(--rose-text); }
  .vertical {
    position: absolute;
    writing-mode: vertical-rl;
    text-orientation: mixed;
    white-space: nowrap;
  }
  .title-en {
    font-family: "Cormorant Garamond", serif;
    font-weight: 300;
    letter-spacing: 0.28em;
  }
  .title-ja {
    font-family: "Noto Serif JP", serif;
    font-weight: 300;
    letter-spacing: 0.35em;
  }
  .cap-spine .title-en {
    top: 265px;
    left: 30px;
    font-size: 27px;
    color: var(--mauve);
  }
  .cap-spine .title-ja {
    top: 528px;
    left: 38px;
    font-size: 11px;
    color: var(--pink-ink);
  }
  .cap-back .title-en {
    top: 250px;
    left: 30px;
    font-size: 36px;
    color: var(--rose-text);
  }
  .cap-back .title-ja {
    top: 515px;
    left: 43px;
    font-size: 13px;
    color: var(--rose-text);
  }
  .tagline {
    font-family: "Noto Serif JP", serif;
    font-weight: 300;
    font-size: 8px;
    letter-spacing: 0.3em;
    color: #c97f93;
  }
  .tagline-one { top: 625px; left: 56px; }
  .tagline-two { top: 650px; left: 40px; }
  .caption {
    position: absolute;
    left: 160px;
    top: 1063px;
    font-family: "Noto Sans JP", sans-serif;
    font-size: 14px;
    color: var(--caption);
    letter-spacing: 0.02em;
    white-space: nowrap;
  }
  .caption .sep { margin: 0 10px; }
</style>
</head>
<body>
  <div class="sheet">
    <div class="sheet-frame"></div>

    <div class="cap">
      <div class="cap-front"></div>

      <div class="cap-spine">
        <div class="brand">
          <span class="brand-dot"></span>
          <span class="brand-name">Marlowe Guild</span>
        </div>
        <span class="vertical title-en">HOTAMINE</span>
        <span class="vertical title-ja">ホタミネ</span>
      </div>

      <div class="cap-back">
        <div class="brand">
          <span class="brand-dot"></span>
          <span class="brand-name">Marlowe Guild</span>
        </div>
        <span class="vertical title-en">HOTAMINE</span>
        <span class="vertical title-ja">ホタミネ</span>
        <span class="vertical tagline tagline-one">春の光に夢をのせて</span>
        <span class="vertical tagline tagline-two">青春の輝きを奏でる</span>
      </div>
    </div>

    <div class="caption">Marlowe Guild様<span class="sep">|</span>CDCap<span class="sep">|</span>55.5mm×120mm</div>
  </div>
</body>
</html>
```